Trendy Mindset Image For Personal Growth Tool

This is our third contest on this design and hoping we get the right image! We have a very specific project to hopefully make it easier for designers to create what we are looking for.
We sell card decks that are personal growth tools. Each card in the deck has a weekly action step that brings users closer to fulfilling their potential in targeted areas. We have decks for helping people around leadership, sustainability, couples, parenting, etc. Please check out www.deckleapro.com for more detail on our products.

This particular tool is for Thought Levers. So, something that depicts a mind/brain that is high functioning and powered up. Please see the "image" attachment. We would love to have this image turned into a mind/brain. We included a couple other types of imagery that might look good as well. The image should also say Thought Levers on it and have the image and we have provided some cool font styels that we like.

Target Market(s)

Middle class, trendy, male/female, millennial types... people interested in personal development, spiritual growth, self improvement.

Colors
3176b5
876aae
33a6d7

Requirements
Must have
• This is for the back of the card that is 5 inches tall and 3.5 inches wide. Must be in CMYK for printing. Title "Thought Levers" as well as some type of image depicting a strong mental state (please see attachemnts).
Nice to have
• Clever designs... very strong preference given to anyone who uses the "image" file attached to create their own design of the mind/brain.
Should not have
• Should not have cartoon type images or anything that depicts masculine or feminine. Would like this to appeal to all. Also, please, no straight copies of stock images. Please provide original work or at least something that is not something exactly the same as someone else's work. It can be a base for your work but looking for something original work here.

```html
<!DOCTYPE html>
<html lang="en">
<head>
<meta charset="utf-8">
<title>Thought Levers – Card Back</title>
<link rel="stylesheet" href="https://fonts.googleapis.com/css2?family=Russo+One&display=swap">
<style>
  :root {
    --page: #ffffff;
    --night: #23203a;
    --night-deep: #1a1830;
    --bolt: #bfe6ff;
    --bolt-core: #ffffff;
    --electric: #33a6d7;
    --royal: #3176b5;
    --violet: #876aae;
    --title-ink: #1e1b33;
    --title-glow: rgba(255, 255, 255, 0.95);
  }
  html, body {
    margin: 0;
    padding: 0;
    width: 1200px;
    height: 1200px;
    overflow: hidden;
    background: var(--page);
  }
  .card-back {
    position: absolute;
    left: 250px;
    top: 100px;
    width: 700px;
    height: 1000px;
    background: var(--night);
    overflow: hidden;
  }
  .lightning-art {
    position: absolute;
    left: 190px;
    top: 0;
    width: 360px;
    height: 1000px;
    background:
      linear-gradient(100deg, transparent 38%, rgba(191, 230, 255, 0.55) 48%, rgba(255,255,255,0.9) 50%, rgba(191, 230, 255, 0.55) 52%, transparent 62%);
    filter: blur(6px);
    opacity: 0.85;
  }
  .burst-art {
    position: absolute;
    left: 40px;
    top: 180px;
    width: 620px;
    height: 580px;
    background:
      radial-gradient(ellipse at center, rgba(255,255,255,0.95) 0%, rgba(220,238,255,0.85) 28%, rgba(135,170,220,0.45) 48%, rgba(35,32,58,0) 70%);
  }
  .brain-orb {
    position: absolute;
    left: 196px;
    top: 317px;
    width: 312px;
    height: 312px;
    border-radius: 50%;
    background:
      radial-gradient(circle at 45% 45%, rgba(51,166,215,0.55) 0%, rgba(49,118,181,0.35) 35%, var(--night-deep) 70%, #0f0e1e 100%);
    box-shadow: 0 0 40px 10px rgba(255,255,255,0.8);
  }
  .card-title {
    position: absolute;
    left: 0;
    width: 700px;
    margin: 0;
    text-align: center;
    font-family: "Russo One", sans-serif;
    font-weight: 400;
    font-size: 68px;
    letter-spacing: 3px;
    line-height: 1;
    color: var(--title-ink);
    text-shadow: 0 0 10px var(--title-glow), 0 0 22px var(--title-glow), 0 0 4px var(--title-glow);
  }
  .card-title--top { top: 286px; }
  .card-title--bottom { top: 646px; }
</style>
</head>
<body>
  <main class="card-back">
    <div class="lightning-art" role="img" aria-label="Lightning bolt running from top to bottom of the card"></div>
    <div class="burst-art" role="img" aria-label="Bright white starburst glow behind the brain"></div>
    <div class="brain-orb" role="img" aria-label="Glowing blue circuit brain inside a dark sphere"></div>
    <h1 class="card-title card-title--top">THOUGHT</h1>
    <p class="card-title card-title--bottom">LEVERS</p>
  </main>
</body>
</html>
```